Church Music Album Cover

We are a Christian church in the OKC metro that is releasing a CD of songs that have connected with our congregation over the past few years. We are a church of about 1500 people of all ages- so while we want the design to be fresh, clean, and attractive- it doesn't have to be overly "youthy" or "edgy." Per the CD distribution company, the art image file you create should be able to be delivered with these requirements met:1400 x 1400 pixels minimum; 3000 x 3000 pixels maximumPNG, GIF, JPG, or JPEG file type72 - 300dpi (300dpi is the best)Less than 25mbRGB color scheme (not CMYK)
Updates

Thanks for submissions thus far. I realize my initial description may have not been the most helpful- and it some ways, I'm not 100% sure what I want. However, I would typically end to stay away from concrete images and tend to lean more towards earthy folk images. I don't even know if that makes sense. One google image search of the word "Grace" brings up individual letters spelling out Grace- each on a card clothes lined to a rope with out of focus lights or candles in the background. Another one had out of focus patio light bulbs lighting up the general text. Not sure why I like those and how they can connect to the theme, but I do. Another one had "Grace" on a pallet wall type background. Hopefully those are helpful suggestions.

Target Market(s)

Young parents- 30-40's

Colors

Requirements
Must have
• Title: Melodies from a Humble Porch
Nice to have
• Earthy/folky themes.
Should not have
• Bright colors

```html
<!DOCTYPE html>
<html lang="en">
<head>
<meta charset="utf-8">
<title>Melodies from a Humble Porch – Album Cover</title>
<link rel="stylesheet" href="https://fonts.googleapis.com/css2?family=Oranienbaum&family=Pinyon+Script&display=swap">
<style>
  :root {
    --page-bg: #fcfbfa;
    --night: #050403;
    --smoke: #1b1917;
    --amber: #e08a1e;
    --amber-soft: rgba(224, 138, 30, 0.55);
    --bulb-warm: #c9a066;
    --ink-light: #ffffff;
    --glow: rgba(255, 196, 110, 0.85);
  }
  * { margin: 0; padding: 0; box-sizing: border-box; }
  html, body {
    width: 1200px;
    height: 790px;
    overflow: hidden;
    background: var(--page-bg);
  }
  .canvas {
    position: relative;
    width: 1200px;
    height: 790px;
  }
  .album-cover {
    position: absolute;
    left: 260px;
    top: 55px;
    width: 680px;
    height: 680px;
    overflow: hidden;
    background: var(--night);
  }
  .cover-photo {
    position: absolute;
    inset: 0;
    background:
      radial-gradient(circle at 20% 62%, var(--bulb-warm) 0, rgba(201,160,102,0.55) 70px, rgba(201,160,102,0) 170px),
      radial-gradient(ellipse 60% 22% at 68% 40%, var(--amber-soft) 0, rgba(224,138,30,0) 100%),
      radial-gradient(ellipse 20% 30% at 5% 45%, rgba(224,138,30,0.4) 0, rgba(224,138,30,0) 100%),
      linear-gradient(180deg, var(--smoke) 0%, var(--night) 45%, var(--smoke) 100%);
  }
  .cover-title {
    position: absolute;
    left: 246px;
    top: 238px;
    width: 414px;
    color: var(--ink-light);
    font-weight: 400;
  }
  .title-lead {
    display: block;
    font-family: "Oranienbaum", serif;
    font-size: 42px;
    line-height: 1;
    letter-spacing: -0.3px;
    white-space: nowrap;
  }
  .title-feature {
    display: block;
    margin-top: 4px;
    margin-left: 6px;
    font-family: "Pinyon Script", cursive;
    font-size: 160px;
    line-height: 1.05;
    white-space: nowrap;
    text-shadow: 0 0 10px var(--glow), 0 0 24px var(--glow);
  }
</style>
</head>
<body>
  <main class="canvas">
    <section class="album-cover">
      <div class="cover-photo" role="img" aria-label="Photograph of a glowing vintage light bulb hanging on a dark cord against a black background with out-of-focus amber string lights"></div>
      <h1 class="cover-title">
        <span class="title-lead">Melodies from a Humble</span>
        <span class="title-feature">Porch</span>
      </h1>
    </section>
  </main>
</body>
</html>
```